Cobalt Bridge Capital - Letterhead

We need letterhead options for our case funding company called Cobalt Bridge Capital. Here are some of the details:

Name - Cobalt Bridge Capital
Phone - (555) 214 - 9087
Address - 58 Harlow Lane
Suite 312
New York, NY 10482
Website - cobaltbridgecapital.example

```html
<!DOCTYPE html>
<html lang="en">
<head>
<meta charset="utf-8">
<title>Cobalt Bridge Capital – Letterhead</title>
<link href="https://fonts.googleapis.com/css2?family=Lato:wght@400;700&family=Yellowtail&display=swap" rel="stylesheet">
<style>
  :root {
    --navy: #0b3556;
    --navy-text: #0e3d5c;
    --slate: #6f8494;
    --ink: #4a4a4a;
    --ink-dark: #222;
    --rule: #9a9a9a;
    --backdrop: #e4e4e4;
    --paper: #ffffff;
  }
  * { box-sizing: border-box; margin: 0; padding: 0; }
  html, body { width: 1200px; height: 1200px; overflow: hidden; }
  body {
    background: var(--backdrop);
    font-family: "Lato", sans-serif;
    position: relative;
  }
  .letterhead {
    position: absolute;
    left: 168px;
    top: 40px;
    width: 864px;
    height: 1120px;
    background: linear-gradient(160deg, var(--paper) 40%, #f1f1f1 100%);
    box-shadow: 0 2px 10px rgba(0,0,0,0.18);
    overflow: hidden;
  }
  .brand {
    position: absolute;
    left: 73px;
    top: 30px;
    display: flex;
    align-items: flex-end;
    gap: 10px;
  }
  .brand-mark {
    width: 56px;
    height: 56px;
    background: var(--navy);
    flex: none;
  }
  .brand-name {
    font-weight: 700;
    font-size: 14px;
    line-height: 15.5px;
    letter-spacing: 2px;
    text-transform: uppercase;
    color: var(--navy);
  }
  .contact {
    position: absolute;
    left: 656px;
    top: 39px;
    padding-left: 13px;
    border-left: 1px solid var(--rule);
    font-size: 13px;
    line-height: 18.3px;
    color: var(--ink);
  }
  .contact .phone {
    display: flex;
    align-items: center;
    gap: 5px;
    margin-top: 8px;
  }
  .contact .phone svg { width: 13px; height: 13px; }
  .letter {
    position: absolute;
    left: 73px;
    top: 290px;
    width: 718px;
  }
  .salutation {
    font-weight: 700;
    font-size: 16px;
    color: var(--navy-text);
    margin-bottom: 18px;
  }
  .letter p.body {
    font-size: 15.8px;
    line-height: 25.3px;
    color: var(--ink);
    text-align: justify;
    margin-bottom: 20px;
  }
  .closing {
    margin-top: 28px;
    font-size: 17.5px;
    color: var(--ink-dark);
  }
  .signature {
    font-family: "Yellowtail", cursive;
    font-size: 32px;
    color: var(--navy-text);
    margin-top: 2px;
  }
  .footer-band {
    position: absolute;
    left: 0;
    bottom: 0;
    width: 864px;
    height: 34px;
  }
  .footer-band svg { position: absolute; inset: 0; }
  .website {
    position: absolute;
    right: 73px;
    top: 7px;
    font-size: 14px;
    letter-spacing: 2.6px;
    color: #fff;
  }
</style>
</head>
<body>
  <main class="letterhead">
    <header>
      <div class="brand">
        <div class="brand-mark"></div>
        <div class="brand-name">Cobalt<br>Bridge<br>Capital</div>
      </div>
      <address class="contact" style="font-style: normal;">
        58 Harlow Lane<br>
        Suite 312<br>
        New York, NY 10482
        <div class="phone">
          <svg viewBox="0 0 16 16" aria-hidden="true">
            <circle cx="8" cy="8" r="7.2" fill="none" stroke="#4a4a4a" stroke-width="1"/>
            <path d="M5.6 4.2c.5-.3 1 .1 1.3.7l.4.9c.1.4 0 .7-.3.9l-.4.3c.3.9.9 1.7 1.7 2.3l.4-.3c.3-.2.6-.2.9 0l.8.6c.5.4.6.9.2 1.3-.9 1-2.5.6-3.9-.9C5.3 8.4 4.6 5.3 5.6 4.2z" fill="#4a4a4a"/>
          </svg>
          (555) 214 - 9087
        </div>
      </address>
    </header>

    <section class="letter">
      <p class="salutation">Dear Mr. Lorem,</p>
      <p class="body">Lorem ipsum dolor sit amet, consectetuer adipiscing elit, sed diam nonummy nibh euismod tinci&shy;dunt ut laoreet dolore magna aliquam erat volutpat. Ut wisi enim ad minim veniam, quis nostrud exerci tation ullamcorper suscipit lobortis nisl ut aliquip ex ea commodo consequat. Duis autem vel eum iriure dolor in hendiusto odio dignissim qui blandit praesent luptatum zzril delenit augue duis dolore te feugait nulla facilisi.</p>
      <p class="body">Lorem ipsum dolor sit amet, consectetuer adipiscing elit, sed diam nonummy nibh euismod tinci&shy;dunt ut laoreet dolore magna aliquam erat volutpat. Ut wisi enim ad minim veniam, quis nostrud exerci tation ullamcorper suscipit lobortis nisl ut aliquip ex ea commodo consequat. Duis autem vel eum iriure dolor in hendiusto odio dignissim qui blandit praesent luptatum zzril delenit augue duis dolore te feugait nulla facilisi.</p>
      <p class="body">Lorem ipsum dolor sit amet, consectetuer adipiscing elit, sed diam nonummy nibh euismod tinci&shy;dunt ut laoreet dolore magna aliquam erat volutpat. Ut wisi enim ad minim veniam, quis nostrud exerci tation ullamcorper suscipit lobortis nisl ut aliquip ex ea commodo consequat. Duis autem vel eum iriure dolor in hendiusto odio dignissim qui blandit praesent luptatum zzril delenit augue duis dolore te feugait nulla facilisi.</p>
      <p class="closing">Sincerely Your,</p>
      <p class="signature">Your Name</p>
    </section>

    <footer class="footer-band">
      <svg viewBox="0 0 864 34" preserveAspectRatio="none" aria-hidden="true">
        <path d="M0 10 H505 C528 10 530 0 556 0 H864 V34 H0 Z" fill="#0b3556"/>
        <path d="M0 10 H505 C515 10 518 12 520 15 C480 18 300 19 0 19 Z" fill="#6f8494"/>
      </svg>
      <span class="website">cobaltbridgecapital.example</span>
    </footer>
  </main>
</body>
</html>
```